New Card

Photography business
I want a sleek simple card that screams rich and classy. Black/Gold or silver font. No photos or images but would love a new logo When I hand someone my card I want compliments
Updates
My fiancé reminded me in 5 short months my name will change so I have changed my name to Colleen Abernathy
Also my BRAND is Lantern Field Photography, not my name. Thanks
Industry/Entity Type
Business
Contact Information for Business Card
Lantern Field Photography
Colleen Abernathy-owner
274 W. Hollis Ave.
Ashgrove Point, NJ 08000
(856)555-0143
colleen@lanternfieldphotos.example
Look and feel
Each slider illustrates characteristics of the customer's brand and the style your logo design should communicate.

```html
<!DOCTYPE html>
<html lang="en">
<head>
<meta charset="utf-8">
<title>Lantern Field Photography – Business Card</title>
<link rel="stylesheet" href="https://fonts.googleapis.com/css2?family=Oswald:wght@500&family=Lato:wght@400;700;900&display=swap">
<style>
  :root {
    --backdrop: #d9d9db;
    --card-black: #050505;
    --gold: #f5a21b;
    --gold-line: #b9861d;
    --white: #ffffff;
    --ink: #111111;
  }
  html, body {
    margin: 0;
    width: 1200px;
    height: 926px;
    overflow: hidden;
    background: var(--backdrop);
  }
  .canvas {
    position: relative;
    width: 1200px;
    height: 926px;
  }
  .card {
    position: absolute;
    top: 314px;
    width: 520px;
    height: 298px;
    background: var(--card-black);
    overflow: hidden;
    box-shadow: 0 10px 28px rgba(0,0,0,.22);
  }
  .card--front { left: 60px; }
  .card--back  { left: 620px; }

  /* front */
  .rule {
    position: absolute;
    height: 1px;
    background: var(--gold-line);
  }
  .rule--top { left: 58px; top: 40px; width: 404px; }
  .rule--low { left: 290px; top: 214px; width: 190px; }
  .mark-dot {
    position: absolute;
    left: 250px;
    top: 30px;
    width: 20px;
    height: 20px;
    border-radius: 50%;
    background: var(--gold);
    box-shadow: 0 0 0 4px var(--card-black);
  }
  .details {
    position: absolute;
    left: 56px;
    top: 56px;
    right: 20px;
  }
  .brand-name {
    margin: 0;
    font-family: 'Oswald', sans-serif;
    font-weight: 500;
    font-size: 27px;
    line-height: 1;
    letter-spacing: 1px;
    text-transform: uppercase;
    color: var(--white);
  }
  .phone {
    margin: 6px 0 0;
    font-family: 'Lato', sans-serif;
    font-weight: 900;
    font-size: 42px;
    line-height: 1;
    letter-spacing: 2px;
    color: var(--white);
  }
  .owner {
    margin: 8px 0 0 28px;
    font-family: 'Lato', sans-serif;
    font-size: 19px;
    letter-spacing: .5px;
    color: var(--white);
  }
  .owner .role { color: var(--gold); }
  .email {
    margin: 4px 0 0 28px;
    font-family: 'Lato', sans-serif;
    font-size: 13px;
    color: var(--white);
  }
  .address-band {
    position: absolute;
    left: 0;
    right: 0;
    bottom: 0;
    height: 58px;
    background: var(--gold);
    display: flex;
    align-items: center;
    justify-content: center;
    font-family: 'Lato', sans-serif;
    font-weight: 700;
    font-size: 16px;
    letter-spacing: 2px;
    text-transform: uppercase;
    white-space: nowrap;
    color: var(--ink);
  }

  /* back */
  .back-lockup {
    position: absolute;
    inset: 0;
    display: flex;
    align-items: center;
    justify-content: center;
    gap: 14px;
  }
  .back-lockup__dot {
    width: 22px;
    height: 22px;
    border-radius: 50%;
    background: var(--gold);
  }
  .back-lockup__name {
    font-family: 'Oswald', sans-serif;
    font-weight: 500;
    font-size: 26px;
    letter-spacing: 1px;
    text-transform: uppercase;
    color: var(--white);
  }
</style>
</head>
<body>
<main class="canvas">
  <section class="card card--front" aria-label="Business card front">
    <div class="rule rule--top"></div>
    <div class="mark-dot"></div>
    <div class="details">
      <h1 class="brand-name">Lantern Field Photography</h1>
      <p class="phone">(856)555-0143</p>
      <p class="owner">Colleen Abernathy-<span class="role">owner</span></p>
      <p class="email">colleen@lanternfieldphotos.example</p>
    </div>
    <div class="rule rule--low"></div>
    <div class="address-band">274 W. Hollis Ave. Ashgrove Point, NJ 08000</div>
  </section>

  <section class="card card--back" aria-label="Business card back">
    <div class="back-lockup">
      <span class="back-lockup__dot"></span>
      <span class="back-lockup__name">Lantern Field Photography</span>
    </div>
  </section>
</main>
</body>
</html>
```